Startup Technology Consulting Firm in NYC Needs A Website

I need a website built for my startup technology consulting company Brightmoor Systems Collective. We offer a unique white glove service that provides end to end technology support. I want to stand out above the rest. We are small firm but are very dedicated which where we derive our name from BSC primarily offers
end to end technology advisory services to small businesses lacking their own IT staff. We offer top notch white glove and our customer service and satisfaction is exceed by no one.

Below are some of what we provide our clients

Strategic IT Planning
Business Continuity Planning/Disaster Recovery
Cloud Computing\DataCenter Solutions
Server Infrastructure/Networking
Virtualization Technologies
Project Management

Our Technology Advisors hold many certifications from Quillora & Tessfold. We are also Quillora Partners

I have attached my logo (preview design) As soon as I ge the final images I will upload.

Reason: want to give more time to submit designs

Industry/Entity Type

Information Technology

Coding

Coded - Design and coding required

Number of Pages Required

1 page

Font styles to use
Sans Serif

Requirements
Must have
• Attract Target Market. The site should bleed the company vision
• DEDICATION everything about the site should show this
• Layout the Benefits of our offerings
• Links to my social media
• Links to dircct my client's for remote support

```html
<!DOCTYPE html>
<html lang="en">
<head>
<meta charset="utf-8">
<title>Brightmoor Systems Collective</title>
<link rel="stylesheet" href="https://fonts.googleapis.com/css2?family=Open+Sans:wght@300;400;600;700&display=swap">
<style>
:root{
  --navy:#163f86;
  --blue:#2456a4;
  --link:#3f7fc4;
  --ink:#2b3038;
  --ink-dark:#23272e;
  --panel:#2f333c;
  --grey-text:#b3b6ba;
  --mid-text:#5e6268;
  --soft:#f1f2f3;
  --pattern:#eceef0;
  --partner-text:#c6c9cc;
  --white:#ffffff;
}
*{margin:0;padding:0;box-sizing:border-box}
html,body{width:1200px;height:3103px;overflow:hidden}
body{position:relative;background:var(--white);font-family:"Open Sans",Arial,sans-serif;color:var(--mid-text)}
.abs{position:absolute}

/* header */
.header{left:0;top:0;width:1200px;height:145px;background:var(--pattern)}
.top-rule{left:45px;top:0;width:1095px;height:12px;background:var(--navy)}
.brand{left:503px;top:12px;width:194px;height:133px;background:#f7f8f9;border-left:1px solid #d9dcdf;border-right:1px solid #d9dcdf;display:flex;flex-direction:column;align-items:center;justify-content:center;gap:8px}
.brand-dot{width:34px;height:34px;border-radius:50%;background:var(--blue)}
.brand-name{font-size:14px;font-weight:600;color:var(--blue);text-align:center;line-height:1.2}

/* nav */
.nav{left:45px;top:145px;width:1095px;height:80px;background:var(--ink);display:flex}
.nav-home{width:83px;height:80px;background:var(--navy);display:flex;align-items:center;justify-content:center}
.nav-item{flex:1;display:flex;align-items:center;justify-content:center;color:var(--white);font-size:12px;font-weight:700;border-left:2px solid #22262c;letter-spacing:.3px}

/* hero */
.hero{left:0;top:225px;width:1200px;height:588px;background:linear-gradient(160deg,#7c90b4 0%,#4e6796 45%,#27395e 100%)}
.hero-title{left:0;top:435px;width:1200px;text-align:center;color:var(--white);font-size:56px;font-weight:400;line-height:74px}
.hero-arrow{width:44px;height:44px;border:2px solid var(--white);border-radius:50%;display:flex;align-items:center;justify-content:center}

/* intro */
.intro-title{left:0;top:906px;width:1200px;text-align:center;color:var(--blue);font-size:45px;font-weight:400;line-height:48px}
.intro-sub{left:0;top:1018px;width:1200px;text-align:center;color:var(--mid-text);font-size:27px;font-weight:400;line-height:30px}
.intro-text{left:190px;top:1123px;width:820px;text-align:center;color:var(--grey-text);font-size:12.5px;line-height:21px}
.btn-find{left:497px;top:1239px;width:206px;height:46px;display:flex}
.btn-find .label{flex:1;background:var(--ink);color:var(--white);font-size:12px;font-weight:700;display:flex;align-items:center;justify-content:center}
.btn-find .icon{width:46px;background:var(--navy);display:flex;align-items:center;justify-content:center}

/* features */
.features{left:0;top:1384px;width:1200px;height:606px;background:var(--soft)}
.feature{width:340px;text-align:center;top:1478px}
.feature-badge{width:114px;height:114px;border-radius:50%;margin:0 auto;display:flex;align-items:center;justify-content:center;color:var(--white);font-size:44px;font-weight:300}
.badge-blue{background:var(--navy)}
.badge-dark{background:var(--ink)}
.feature-title{margin-top:24px;font-size:28px;font-weight:300;color:var(--ink);line-height:29px;height:58px}
.feature-tag{margin-top:16px;font-size:13px;font-weight:600;color:var(--link)}
.feature-text{margin:14px auto 0;width:330px;font-size:12.5px;line-height:21px;color:var(--grey-text);height:63px}
.feature-plus{width:42px;height:42px;background:var(--ink);margin:56px auto 0;display:flex;align-items:center;justify-content:center}

/* newsletter */
.newsletter{left:0;top:1990px;width:1200px;height:257px;background:var(--panel)}
.newsletter-title{left:0;top:2044px;width:1200px;text-align:center;color:var(--white);font-size:45px;font-weight:300}
.email-field{left:478px;top:2141px;width:201px;height:46px;background:var(--white);font-size:10px;color:#a7aaae;display:flex;align-items:center;padding-left:18px}
.email-go{left:681px;top:2141px;width:45px;height:46px;background:var(--navy);color:var(--white);font-size:12px;font-weight:700;display:flex;align-items:center;justify-content:center}
.support-bar{left:0;top:2247px;width:1200px;height:68px;background:var(--ink-dark);color:var(--white);font-size:17px;display:flex;align-items:center;justify-content:center}
.support-bar .hl{color:var(--link);margin-left:5px}

/* about & news */
.section-title{font-size:28px;font-weight:300;color:var(--ink)}
.about-photo{left:52px;top:2483px;width:159px;height:159px;background:linear-gradient(135deg,#e9d9c8,#c9a98c);border:1px solid #e2e2e2}
.about-name{left:240px;top:2480px;font-size:13px;color:var(--ink)}
.about-lead{left:240px;top:2504px;width:430px;font-size:17.5px;color:var(--blue);line-height:24px}
.about-text{font-size:12px;line-height:21px;color:var(--grey-text)}
.news-item{left:801px;width:350px;height:88px}
.news-date{left:0;top:0;width:72px;height:88px;background:var(--navy);color:var(--white);text-align:center}
.news-date .day{font-size:34px;font-weight:300;line-height:48px;margin-top:10px}
.news-date .mon{font-size:12px}
.news-date::after{content:"";position:absolute;right:-12px;top:22px;border-left:12px solid var(--navy);border-top:11px solid transparent;border-bottom:11px solid transparent}
.news-title{left:95px;top:0;font-size:16px;font-weight:400;color:var(--ink)}
.news-tag{left:95px;top:24px;font-size:13px;color:var(--link)}
.news-text{left:95px;top:48px;width:250px;font-size:12px;line-height:21px;color:var(--grey-text)}
.news-sep{left:801px;top:2605px;width:350px;height:1px;background:#e6e7e9}

/* partners */
.partners{left:0;top:2824px;width:1200px;height:149px;background:#f4f5f6;display:flex}
.partner{flex:1;display:flex;align-items:center;justify-content:center;gap:12px;border-right:2px solid #fbfbfc;color:var(--partner-text);font-size:34px;font-weight:300}
.partner .mark{width:26px;height:26px;border-radius:50%;background:#d2d5d8}
.partner.small{font-size:20px}

/* footer */
.footer{left:0;top:2973px;width:1200px;height:130px;background:var(--pattern)}
.copyright{left:66px;top:3038px;font-size:13px;color:var(--mid-text)}
.social{left:988px;top:3032px;display:flex;gap:12px}
.social span{width:30px;height:30px;border-radius:50%;background:var(--ink)}
</style>
</head>
<body>

<header>
  <div class="abs header"></div>
  <div class="abs top-rule"></div>
  <div class="abs brand">
    <span class="brand-dot"></span>
    <span class="brand-name">Brightmoor Systems<br>Collective</span>
  </div>
  <nav class="abs nav">
    <a class="nav-home" aria-label="Home">
      <svg width="36" height="30" viewBox="0 0 36 30"><path d="M18 2 2 16h5v12h8v-8h6v8h8V16h5z" fill="#fff"/></svg>
    </a>
    <a class="nav-item">PLANNING</a>
    <a class="nav-item">CLOUD</a>
    <a class="nav-item">SERVICES</a>
    <a class="nav-item">BLOG</a>
    <a class="nav-item">CONTACTS</a>
  </nav>
</header>

<section>
  <div class="abs hero" role="img" aria-label="Office desk with computer keyboard and monitors in blue tones"></div>
  <h1 class="abs hero-title">WE ARE EXPERIENCED IN ALL<br>ASPECTS OF ENTERPRISE IT</h1>
  <a class="abs hero-arrow" style="left:65px;top:499px" aria-label="Previous">
    <svg width="14" height="14" viewBox="0 0 14 14"><path d="M9 2 4 7l5 5" stroke="#fff" stroke-width="2" fill="none"/></svg>
  </a>
  <a class="abs hero-arrow" style="left:1089px;top:499px" aria-label="Next">
    <svg width="14" height="14" viewBox="0 0 14 14"><path d="m5 2 5 5-5 5" stroke="#fff" stroke-width="2" fill="none"/></svg>
  </a>
</section>

<section>
  <h2 class="abs intro-title">OUR ADVISORS ARE AT THE CORE OF YOUR IT<br>END TO END SUPPORT, DELIVERED WITH CARE</h2>
  <p class="abs intro-sub">WE HELP SMALL BUSINESSES WITHOUT IT STAFF PLAN,<br>BUILD AND PROTECT THE SYSTEMS THEY RELY ON.</p>
  <p class="abs intro-text">Brightmoor Systems Collective offers white glove technology advisory for small businesses. From strategic IT planning and business continuity to server infrastructure, networking and project management, one dedicated team handles every step. Our advisors hold certifications from Quillora and Tessfold, and as Quillora Partners we bring proven tools to every client, with service and satisfaction that set us apart.</p>
  <a class="abs btn-find">
    <span class="label">FIND OUT MORE</span>
    <span class="icon"><svg width="20" height="20" viewBox="0 0 20 20"><circle cx="8" cy="8" r="6" stroke="#fff" stroke-width="2.5" fill="none"/><path d="m12.5 12.5 5 5" stroke="#fff" stroke-width="3"/></svg></span>
  </a>
</section>

<section>
  <div class="abs features"></div>
  <div class="abs feature" style="left:55px">
    <div class="feature-badge badge-blue">A</div>
    <h3 class="feature-title">STRATEGIC IT<br>PLANNING</h3>
    <p class="feature-tag">ROADMAPS AND CONTINUITY</p>
    <p class="feature-text">Clear technology roadmaps, budgets and disaster recovery plans that keep your business running through any outage or change.</p>
    <a class="feature-plus"><svg width="14" height="14" viewBox="0 0 14 14"><path d="M7 1v12M1 7h12" stroke="#fff" stroke-width="2"/></svg></a>
  </div>
  <div class="abs feature" style="left:430px">
    <div class="feature-badge badge-blue">B</div>
    <h3 class="feature-title">CLOUD &amp; DATA<br>CENTER SOLUTIONS</h3>
    <p class="feature-tag">SERVERS AND NETWORKING</p>
    <p class="feature-text">Cloud migrations, server infrastructure and secure networks designed, installed and looked after by one dedicated team.</p>
    <a class="feature-plus"><svg width="14" height="14" viewBox="0 0 14 14"><path d="M7 1v12M1 7h12" stroke="#fff" stroke-width="2"/></svg></a>
  </div>
  <div class="abs feature" style="left:805px">
    <div class="feature-badge badge-dark">C</div>
    <h3 class="feature-title">VIRTUALIZATION<br>TECHNOLOGIES</h3>
    <p class="feature-tag">PROJECT MANAGEMENT</p>
    <p class="feature-text">Certified advisors consolidate your systems and manage each project from first plan to final handover, on time and on budget.</p>
    <a class="feature-plus"><svg width="14" height="14" viewBox="0 0 14 14"><path d="M7 1v12M1 7h12" stroke="#fff" stroke-width="2"/></svg></a>
  </div>
</section>

<section>
  <div class="abs newsletter"></div>
  <h2 class="abs newsletter-title">NEWSLETTER</h2>
  <div class="abs email-field">ENTER EMAIL</div>
  <a class="abs email-go">GO!</a>
  <div class="abs support-bar">NEED HELP WITH YOUR SYSTEMS? REACH AN ADVISOR NOW WITH <span class="hl">REMOTE SUPPORT! START A SESSION</span></div>
</section>

<section>
  <h2 class="abs section-title" style="left:52px;top:2405px">SHORTLY ABOUT US</h2>
  <div class="abs about-photo" role="img" aria-label="Portrait photo of a technology advisor"></div>
  <p class="abs about-name">MARLA STENHOLM</p>
  <p class="abs about-lead">WHITE GLOVE SERVICE FROM ADVISORS CERTIFIED BY QUILLORA AND TESSFOLD.</p>
  <p class="abs about-text" style="left:240px;top:2565px;width:480px">We started Brightmoor Systems Collective to give small businesses the kind of technology care usually kept for large firms. Every client has a named advisor who knows their systems, answers quickly and stays with each project until it is done right. Dedication is how we work, every day and on every call.</p>
  <p class="abs about-text" style="left:52px;top:2660px;width:668px">From the first planning meeting to ongoing support, we look after strategy, continuity, cloud, servers, networks and virtualization, so owners can focus on their customers while we focus on the systems that keep them running.</p>

  <h2 class="abs section-title" style="left:801px;top:2405px">FEATURED NEWS</h2>
  <article class="abs news-item" style="top:2479px">
    <div class="abs news-date"><div class="day">01</div><div class="mon">AUG</div></div>
    <h4 class="abs news-title">QUILLORA PARTNER STATUS</h4>
    <p class="abs news-tag">COMPANY NEWS</p>
    <p class="abs news-text">We are proud to be named Quillora Partners for another year of service.</p>
  </article>
  <div class="abs news-sep"></div>
  <article class="abs news-item" style="top:2634px">
    <div class="abs news-date"><div class="day">02</div><div class="mon">AUG</div></div>
    <h4 class="abs news-title">NEW RECOVERY PLANS</h4>
    <p class="abs news-tag">CONTINUITY</p>
    <p class="abs news-text">Disaster recovery packages now sized for teams of five to fifty.</p>
  </article>
</section>

<section class="abs partners">
  <div class="partner">Varnel</div>
  <div class="partner"><span class="mark"></span>Quisto</div>
  <div class="partner"><span class="mark"></span>Brenwick</div>
  <div class="partner small"><span class="mark"></span>ORCHARD LAB</div>
</section>

<footer>
  <div class="abs footer"></div>
  <p class="abs copyright">© 2015 | Privacy policy</p>
  <div class="abs social" aria-label="Social media links">
    <span></span><span></span><span></span><span></span>
  </div>
</footer>

</body>
</html>
```